Larchmoor Farm Brochure

To design a small brochure that tells people about our U-Pick cherry farm, where we are, when we are open and what our contact details are.

We have existing logo's which should be used. I have uploaded a file with these details.

Details about us are all located on:-
www.huddlepage.net/larchmoorfarm
https://circles.quorvane.net/u/0/b/570918346627304519837/570918346627304519837/about/p/pub

Farm

```html
<!DOCTYPE html>
<html lang="en">
<head>
<meta charset="utf-8">
<title>Larchmoor Farm Brochure</title>
<link href="https://fonts.googleapis.com/css2?family=Lato:ital,wght@0,400;0,700;0,900;1,700&family=Arimo:wght@400&display=swap" rel="stylesheet">
<style>
  :root {
    --green-deep: #0b7d5f;
    --green: #13a07a;
    --green-light: #2cbf92;
    --lime: #a8d21c;
    --lime-dark: #7fb314;
    --lime-pale: #d8ee7a;
    --white: #ffffff;
    --ink: #333333;
    --paper: #f7f8f5;
    --page-bg: #e6e6e3;
  }
  * { box-sizing: border-box; margin: 0; padding: 0; }
  html, body { width: 900px; height: 1200px; overflow: hidden; }
  body { background: var(--page-bg); font-family: "Lato", sans-serif; position: relative; }

  .spread { position: absolute; left: 100px; width: 705px; height: 500px; overflow: hidden;
            box-shadow: 0 4px 14px rgba(0,0,0,.18); }
  .spread--outside { top: 60px; }
  .spread--inside { top: 640px; height: 495px; }
  .spread__shapes { position: absolute; inset: 0; }

  .pill { position: absolute; background: var(--white); color: var(--green-deep);
          font-weight: 700; border-radius: 0 14px 14px 0; display: flex; align-items: center; }
  .pill--url { border-radius: 14px; font-size: 13px; justify-content: center; }
  .pill--dark { background: var(--green-deep); color: var(--white); }
  .heading { font-size: 23px; font-weight: 900; padding-left: 18px; }

  .about { position: absolute; left: 18px; top: 212px; width: 220px; color: var(--white);
           font-size: 9.5px; line-height: 13px; }
  .about p + p { margin-top: 7px; }
  .about__quote { margin-top: 16px; color: var(--lime-pale); font-style: italic; font-weight: 700;
                  font-size: 11px; line-height: 13.5px; }
  .about__sign { margin-top: 10px; text-align: right; font-weight: 700; font-size: 12px; }

  .hours { position: absolute; left: 301px; top: 202px; width: 104px; height: 104px; border-radius: 50%;
           background: var(--white); border: 4px solid var(--lime); text-align: center;
           display: flex; flex-direction: column; justify-content: center; color: var(--ink);
           box-shadow: 0 3px 6px rgba(0,0,0,.25); }
  .hours__title { color: var(--green-deep); font-weight: 900; font-size: 13px; }
  .hours__days { font-size: 10px; line-height: 12px; }
  .hours__days--big { font-size: 13px; line-height: 15px; }
  .hours__time { color: var(--green-deep); font-weight: 900; font-size: 13px; }

  .contact { position: absolute; left: 255px; top: 407px; width: 200px; color: var(--white);
             font-size: 11px; line-height: 14px; text-align: center; }
  .contact li { list-style: none; margin-bottom: 6px; }
  .contact__icon { display: inline-block; width: 7px; height: 7px; border-radius: 50%;
                   background: var(--lime); margin-right: 6px; vertical-align: middle; }

  .brand { position: absolute; left: 490px; top: 350px; width: 200px; text-align: center;
           color: var(--white); font-weight: 400; line-height: 1; }
  .brand__line1 { font-size: 40px; display: block; }
  .brand__line2 { font-size: 26px; display: block; margin-top: 2px; }

  .story { position: absolute; left: 18px; top: 83px; width: 210px; color: var(--ink);
           font-family: "Arimo", sans-serif; font-size: 12.3px; line-height: 15px; }
  .story p + p { margin-top: 15px; }
  .details { position: absolute; left: 487px; top: 40px; width: 200px; color: var(--ink);
             font-family: "Arimo", sans-serif; font-size: 12.3px; line-height: 15px; }
  .details p + p { margin-top: 15px; }

  .photo { position: absolute; left: 253px; width: 182px; height: 97px; border-radius: 12px;
           border: 3px solid var(--lime); box-shadow: 0 3px 6px rgba(0,0,0,.25); }
  .photo--hives { top: 40px; background: linear-gradient(180deg, #4e7d3a 0%, #6b9a3f 45%, #8dbb4e 100%); }
  .photo--cherries { top: 172px; background: radial-gradient(circle at 40% 55%, #d8202a 0%, #a10f18 55%, #5d0a0e 100%); }
  .photo--orchard { top: 303px; background: linear-gradient(180deg, #8fbfe6 0%, #b9d4e6 45%, #7a7a55 65%, #6f9a3d 100%); }
</style>
</head>
<body>

<!-- Outside of the brochure -->
<section class="spread spread--outside" aria-label="Brochure outside">
  <svg class="spread__shapes" viewBox="0 0 705 500" width="705" height="500">
    <defs>
      <linearGradient id="outBg" x1="0" y1="0" x2="0" y2="1">
        <stop offset="0" stop-color="#17a882"/>
        <stop offset="1" stop-color="#0b7d5f"/>
      </linearGradient>
      <linearGradient id="outPhoto" x1="0" y1="0" x2="0" y2="1">
        <stop offset="0" stop-color="#9fc3e0"/>
        <stop offset="0.22" stop-color="#4d6b4a"/>
        <stop offset="0.45" stop-color="#7aa845"/>
        <stop offset="1" stop-color="#5f8a2e"/>
      </linearGradient>
      <linearGradient id="limeBand" x1="0" y1="0" x2="1" y2="0">
        <stop offset="0" stop-color="#e8f5b0"/>
        <stop offset="0.5" stop-color="#b8dc3a"/>
        <stop offset="1" stop-color="#8fc01a"/>
      </linearGradient>
    </defs>
    <rect width="705" height="500" fill="url(#outBg)"/>
    <path d="M140,0 C165,130 270,255 440,282 L705,282 L705,340 L430,340 C250,325 160,210 128,0 Z" fill="url(#limeBand)"/>
    <path d="M140,0 C170,125 275,250 440,268 L705,268 L705,282 L440,282 C270,255 165,130 140,0 Z" fill="#ffffff" opacity=".9"/>
    <path d="M150,0 C180,120 285,245 445,260 L705,260 L705,0 Z" fill="url(#outPhoto)" role="img" aria-label="Photo of young cherry trees in rows with a dam, hills and forest behind"/>
    <rect x="240" y="0" width="6" height="500" fill="#000" opacity=".05"/>
    <rect x="472" y="0" width="6" height="500" fill="#000" opacity=".05"/>
    <rect x="0" y="490" width="705" height="10" fill="var(--lime)"/>
    <rect x="276" y="330" width="155" height="61" fill="#ecebe6" stroke="#cfcfc8" role="img" aria-label="Street map showing the farm location"/>
  </svg>

  <div class="pill heading" style="left:0;top:162px;width:168px;height:29px;">About us</div>
  <div class="about">
    <p>Larchmoor Farm is in the beautiful Yarra Valley, an ideal location for growing sweet juicy cherries. Visit us for Pick Your Own or Pre-Picked Cherries.</p>
    <p>When you first arrive at our farm we can show you how to pick cherries and where the best cherries are on that day. Farmer Tom can also show you around the farm and explain how the cherries are grown and the organic principles we employ in managing our trees.</p>
    <p class="about__quote">It's the magnificent views and our happy trees. That's what makes our cherries juicier and sweeter.</p>
    <p class="about__sign">-Farmer Tom</p>
  </div>
  <div class="pill pill--url" style="left:0;top:452px;width:212px;height:28px;border-radius:0 14px 14px 0;">www.larchmoorfarm.com.au</div>

  <div class="hours">
    <span class="hours__title">We are Open</span>
    <span class="hours__days">Friday, Saturday</span>
    <span class="hours__days hours__days--big">and Sunday</span>
    <span class="hours__time">10am to 5pm</span>
  </div>

  <ul class="contact">
    <li><span class="contact__icon"></span>18 Ridgeway Orchard Road, Kellsbrook, Victoria 3187</li>
    <li><span class="contact__icon"></span>1300 48 00 91</li>
    <li><span class="contact__icon"></span>www.larchmoorfarm.com.au</li>
  </ul>

  <div class="brand">
    <span class="brand__line1">Larchmoor</span>
    <span class="brand__line2">Farm</span>
  </div>
  <div class="pill pill--url" style="left:506px;top:458px;width:170px;height:22px;font-size:11px;">www.larchmoorfarm.com.au</div>
</section>

<!-- Inside of the brochure -->
<section class="spread spread--inside" aria-label="Brochure inside">
  <svg class="spread__shapes" viewBox="0 0 705 495" width="705" height="495">
    <defs>
      <linearGradient id="midBg" x1="0" y1="0" x2="0" y2="1">
        <stop offset="0" stop-color="#17a882"/>
        <stop offset="1" stop-color="#0b7d5f"/>
      </linearGradient>
      <linearGradient id="waveLime" x1="0" y1="0" x2="1" y2="0">
        <stop offset="0" stop-color="#b8dc3a"/>
        <stop offset="1" stop-color="#8fc01a"/>
      </linearGradient>
    </defs>
    <rect width="705" height="495" fill="var(--paper)"/>
    <rect x="235" y="0" width="230" height="495" fill="url(#midBg)"/>
    <path d="M0,425 C200,440 420,440 705,300 L705,495 L0,495 Z" fill="#ffffff"/>
    <path d="M0,432 C200,448 430,445 705,312 L705,495 L0,495 Z" fill="url(#waveLime)"/>
    <path d="M0,455 C220,468 440,462 705,370 L705,495 L0,495 Z" fill="var(--lime-dark)" opacity=".5"/>
  </svg>

  <div class="pill heading" style="left:0;top:36px;width:125px;height:29px;background:var(--green);color:var(--white);">STORY</div>
  <div class="story">
    <p>Larchmoor Farm is in the beautiful Yarra Valley, an ideal location for growing sweet juicy cherries. Visit us for Pick Your Own or Pre-Picked Cherries.</p>
    <p>When picking, you can eat as much as you want. Prices for take away U-Pick fruit is $8 per kilo. There are no entry fees.</p>
    <p>Visitors are welcome to picnic beside our scenic dam and enjoy the views of the valley, the neighboring vineyards and the distant mountain ranges.</p>
    <p>Cherries have been grown at Larchmoor Farm for the last 50 or so years. Some of our trees today date back to these original plantings.</p>
  </div>

  <div class="photo photo--hives" role="img" aria-label="Photo of beehives lined up on a grassy slope beside trees"></div>
  <div class="photo photo--cherries" role="img" aria-label="Close-up photo of ripe red cherries with water drops"></div>
  <div class="photo photo--orchard" role="img" aria-label="Photo of bare cherry trees in winter rows under a blue sky"></div>

  <div class="details">
    <p>Our cherry trees are pruned to enable easy picking for people of all ages. We have over 4,000 trees which ensures we always have more than plenty of juicy ripe fruit to pick.</p>
    <p>We have 12 varieties of cherries, most of which are heritage varieties and are rarely found elsewhere. Some have dark, near black fruit, some have bright mahogany sweet highly juicy fruit and others have red firm fruit. Our cherries are known as mid-season cherries and are typically available in November and December, sometimes still available at the beginning of January.</p>
  </div>

  <div class="pill pill--url pill--dark" style="left:30px;top:452px;width:168px;height:22px;font-size:12px;">www.larchmoorfarm.com.au</div>
  <div class="pill pill--url pill--dark" style="left:268px;top:452px;width:168px;height:22px;font-size:12px;">www.larchmoorfarm.com.au</div>
  <div class="pill pill--url pill--dark" style="left:495px;top:452px;width:168px;height:22px;font-size:12px;">www.larchmoorfarm.com.au</div>
</section>

</body>
</html>
```